Brightwell Surface Care - Business Card Design

Use company logo and design a new business card. We are looking for a front and back design. The back should be a dark purple background. We want the back to show cartoon-like soap bubbles chasing mildew cartoon shaped figures. This gives the idea that Brightwell Surface Care provides exterior washing services that work. No mildew stands a chance when Brightwell Surface Care shows up to work. The mildew cartoon images should be green in color, have eyes, and look scared of the bubbles. The bubbles should be light blue in color and have eyes that looked excited to be there.
We will advertise on Mingleport and Pixelvine. These Mingleport and Pixelvine icons should be somewhere on the card.

```html
<!DOCTYPE html>
<html lang="en">
<head>
<meta charset="utf-8">
<title>Brightwell Surface Care – Business Card</title>
<link rel="stylesheet" href="https://fonts.googleapis.com/css2?family=Montserrat:wght@400;500;700;800&display=swap">
<style>
  :root {
    --page: #e6e6ea;
    --purple: #3a1f5e;
    --purple-soft: #4a3178;
    --foam: #95dffc;
    --foam-shade: #6fbcd8;
    --bubble: #b9e9ff;
    --mildew: #8cc43f;
    --white: #ffffff;
  }
  * { margin: 0; padding: 0; box-sizing: border-box; }
  html, body { width: 1200px; height: 1200px; overflow: hidden; }
  body {
    background: var(--page);
    font-family: "Montserrat", sans-serif;
    position: relative;
  }
  .card {
    position: absolute;
    left: 150px;
    width: 900px;
    height: 514px;
    border-radius: 36px;
    overflow: hidden;
    box-shadow: 0 10px 30px rgba(0,0,0,0.18);
  }
  .card--back { top: 52px; background: var(--purple); }
  .card--front { top: 634px; background: var(--white); }

  /* back side */
  .brand {
    position: absolute;
    left: 70px;
    top: 110px;
    color: var(--white);
  }
  .brand__name {
    font-weight: 800;
    font-size: 64px;
    line-height: 1;
    letter-spacing: -1px;
  }
  .brand__tag {
    margin-top: 10px;
    font-weight: 700;
    font-size: 19px;
    letter-spacing: 3px;
    text-transform: uppercase;
  }
  .artwork {
    position: absolute;
    left: 450px;
    top: 70px;
    width: 410px;
    height: 230px;
    border-radius: 28px;
    background: linear-gradient(100deg, var(--bubble) 0%, #7fb8c9 55%, var(--mildew) 100%);
    opacity: 0.9;
  }
  .foam {
    position: absolute;
    left: 0;
    bottom: 0;
    width: 900px;
    height: 260px;
  }
  .contact {
    position: absolute;
    left: 90px;
    bottom: 40px;
    list-style: none;
    color: var(--purple);
    font-size: 22px;
    font-weight: 500;
  }
  .contact__item {
    display: flex;
    align-items: center;
    gap: 12px;
    height: 36px;
  }
  .contact__icon { width: 24px; height: 24px; flex: none; }
  .social-box {
    width: 22px; height: 22px;
    border: 2.5px solid var(--purple);
    border-radius: 5px;
    flex: none;
  }
  .social-name { font-weight: 500; }

  /* front side */
  .logo {
    position: absolute;
    left: 0; right: 0;
    top: 165px;
    text-align: center;
    color: var(--purple);
  }
  .logo__name {
    font-weight: 800;
    font-size: 110px;
    line-height: 1;
    letter-spacing: -2px;
  }
  .logo__tag {
    margin-top: 16px;
    font-weight: 700;
    font-size: 32px;
    letter-spacing: 6px;
    text-transform: uppercase;
    color: var(--purple-soft);
  }
</style>
</head>
<body>

<section class="card card--back">
  <div class="brand">
    <div class="brand__name">Brightwell</div>
    <div class="brand__tag">Surface Care</div>
  </div>

  <div class="artwork" role="img" aria-label="Cartoon of an excited light blue soap bubble chasing scared green mildew figures, with floating bubbles"></div>

  <svg class="foam" viewBox="0 0 900 260" preserveAspectRatio="none" aria-hidden="true">
    <path d="M0 60 C 120 10, 260 20, 330 90 C 360 30, 450 10, 500 50 C 560 20, 640 30, 700 120 L 780 260 L 0 260 Z" fill="var(--foam-shade)"/>
    <path d="M0 68 C 120 20, 255 30, 322 98 C 355 40, 445 22, 492 62 C 555 30, 630 42, 688 128 L 770 260 L 0 260 Z" fill="var(--foam)"/>
    <rect x="0" y="128" width="900" height="132" fill="var(--foam)"/>
  </svg>

  <ul class="contact">
    <li class="contact__item">
      <svg class="contact__icon" viewBox="0 0 24 24"><path d="M6.6 10.8a15 15 0 0 0 6.6 6.6l2.2-2.2c.3-.3.7-.4 1-.2 1.1.4 2.3.6 3.6.6.6 0 1 .4 1 1V20c0 .6-.4 1-1 1A17 17 0 0 1 3 4c0-.6.4-1 1-1h3.5c.6 0 1 .4 1 1 0 1.3.2 2.5.6 3.6.1.3 0 .7-.2 1z" fill="var(--purple)"/></svg>
      <span>(000) 000 0000</span>
    </li>
    <li class="contact__item">
      <svg class="contact__icon" viewBox="0 0 24 24"><rect x="2" y="5" width="20" height="14" rx="1" fill="var(--purple)"/><path d="M3 6l9 7 9-7" stroke="var(--foam)" stroke-width="1.8" fill="none"/></svg>
      <span>email@youremail.com</span>
    </li>
    <li class="contact__item">
      <svg class="contact__icon" viewBox="0 0 24 24" fill="none" stroke="var(--purple)" stroke-width="2"><circle cx="12" cy="12" r="9.5"/><ellipse cx="12" cy="12" rx="4.5" ry="9.5"/><path d="M2.5 12h19M4 7h16M4 17h16"/></svg>
      <span>www.yourwebsite.com</span>
    </li>
    <li class="contact__item">
      <span class="social-box"></span><span class="social-name">Pixelvine</span>
      <span class="social-box"></span><span class="social-name">Mingleport</span>
      <span>@brightwellsurface</span>
    </li>
  </ul>
</section>

<section class="card card--front">
  <div class="logo">
    <div class="logo__name">Brightwell</div>
    <div class="logo__tag">Surface Care</div>
  </div>
</section>

</body>
</html>
```